Business card design and logo for plumbing bussiness

We are wanting a logo for a plumbing business is Queensland Australia. KRV Plumbing and Drainage will be doing works on domestic and commercial sites.
Plumbing, drainage and gas works. We are wanting something that will stand out and be noticed. Colours could be black blue and white but open for suggestions.

Target Market(s)

Builders and home renovators

Industry/Entity Type

Plumbing

Contact Information for Business Card

Miles Dorgan - Director
0417 582 913
miles@krvplumbing.example.com.au
QBCC: 847 2106
ABN: 52 319 407 281

Font styles to use
Sans Serif

Colors
000000

Requirements
Must have
• Clear defined branding

```html
<!DOCTYPE html>
<html lang="en">
<head>
<meta charset="utf-8">
<title>KRV Plumbing and Drainage – Business Card</title>
<link rel="stylesheet" href="https://fonts.googleapis.com/css2?family=Michroma&family=Open+Sans:wght@400;600&display=swap">
<style>
  :root {
    --page-bg: #e4e4e2;
    --card-black: #050608;
    --card-glow: #1a2330;
    --brand-blue: #2f7fd8;
    --tag-blue: #2a6cc0;
    --text-white: #f2f4f7;
    --text-soft: #c9cfd8;
    --rule-grey: #59606b;
  }
  * { box-sizing: border-box; margin: 0; padding: 0; }
  html, body {
    width: 1200px; height: 784px; overflow: hidden;
    background: var(--page-bg);
    font-family: "Open Sans", Arial, sans-serif;
  }
  .canvas { position: relative; width: 1200px; height: 784px; }

  .card {
    position: absolute;
    width: 620px; height: 354px;
    background:
      radial-gradient(ellipse 55% 70% at 50% 38%, var(--card-glow) 0%, transparent 70%),
      radial-gradient(circle, rgba(255,255,255,0.035) 1px, transparent 1.5px) 0 0 / 5px 5px,
      var(--card-black);
    box-shadow: 0 10px 24px rgba(0,0,0,0.25);
    overflow: hidden;
  }
  .card--front { left: 90px; top: 40px; }
  .card--back  { left: 490px; top: 400px; }

  /* Brand lockup */
  .brand { position: absolute; display: flex; flex-direction: column; align-items: center; }
  .brand__disc {
    width: 92px; height: 92px; border-radius: 50%;
    background: var(--brand-blue);
  }
  .brand__name {
    margin-top: 16px;
    color: var(--text-white);
    font-weight: 600; font-size: 24px; letter-spacing: 3px;
    text-transform: uppercase; white-space: nowrap;
  }
  .card--front .brand { left: 0; right: 0; top: 54px; }
  .card--back .brand { left: 90px; top: 118px; }
  .card--back .brand__disc { width: 100px; height: 100px; }
  .card--back .brand__name { font-size: 18px; }

  .tagline {
    position: absolute; left: 0; right: 0; top: 244px;
    text-align: center;
    font-family: "Michroma", Arial, sans-serif;
    color: var(--tag-blue);
    font-size: 12px; letter-spacing: 4px; line-height: 22px;
    text-transform: uppercase;
  }

  /* Contact block */
  .divider {
    position: absolute; left: 330px; top: 80px;
    width: 1px; height: 200px; background: var(--rule-grey);
  }
  .contact { position: absolute; left: 352px; top: 92px; }
  .contact__name { color: var(--brand-blue); font-weight: 600; font-size: 19px; }
  .contact__role { color: var(--text-soft); font-size: 11px; margin-top: 1px; }
  .contact__list { list-style: none; margin-top: 26px; color: var(--text-white); font-size: 13px; line-height: 19px; }
  .contact__list li { display: flex; align-items: center; gap: 6px; padding-left: 18px; }
  .contact__list li.has-icon { padding-left: 0; }
  .contact__icon { width: 12px; height: 12px; flex: none; }
</style>
</head>
<body>
<main class="canvas">

  <section class="card card--front" aria-label="Card front">
    <div class="brand">
      <div class="brand__disc"></div>
      <div class="brand__name">KRV Plumbing</div>
    </div>
    <p class="tagline">Domestic and commercial<br>Plumbing, drainage and gas works</p>
  </section>

  <section class="card card--back" aria-label="Card back">
    <div class="brand">
      <div class="brand__disc"></div>
      <div class="brand__name">KRV Plumbing</div>
    </div>
    <div class="divider"></div>
    <div class="contact">
      <p class="contact__name">Miles Dorgan</p>
      <p class="contact__role">Director</p>
      <ul class="contact__list">
        <li class="has-icon">
          <svg class="contact__icon" viewBox="0 0 12 12" aria-hidden="true"><path d="M2.5 1 L4.5 1 L5.2 3.6 L4 4.6 Q5 6.9 7.4 8 L8.4 6.8 L11 7.5 L11 9.5 Q10.5 11 9 11 Q1 10 1 3 Q1 1.5 2.5 1 Z" fill="#2f7fd8"/></svg>
          0417 582 913
        </li>
        <li class="has-icon">
          <svg class="contact__icon" viewBox="0 0 12 12" aria-hidden="true"><rect x="0.5" y="2.5" width="11" height="7.5" rx="1" fill="#2f7fd8"/><path d="M1 3 L6 7 L11 3" stroke="#050608" stroke-width="1" fill="none"/></svg>
          miles@krvplumbing.example.com.au
        </li>
        <li>QBCC: 847 2106</li>
        <li>ABN: 52 319 407 281</li>
      </ul>
    </div>
  </section>

</main>
</body>
</html>
```